QTR business cards

I need a Business card design for my self. I am behavior analyst owner of a new company based in Miami. We offer Applied Behavior Analysis (ABA) services to individuals with developmental disabilities.

Business

```html
<!DOCTYPE html>
<html lang="en">
<head>
<meta charset="utf-8">
<title>QTR Business Cards</title>
<link href="https://fonts.googleapis.com/css2?family=Lato:wght@400;700;900&display=swap" rel="stylesheet">
<style>
  :root {
    --navy: #1d4481;
    --navy-text: #1f4e8c;
    --leaf: #4fa843;
    --paper: #ffffff;
    --stage: #ecebe8;
  }
  * { margin: 0; padding: 0; box-sizing: border-box; }
  html, body {
    width: 1200px;
    height: 1000px;
    overflow: hidden;
    background: var(--stage);
    font-family: "Lato", sans-serif;
  }
  .card {
    position: absolute;
    left: 300px;
    width: 600px;
    height: 340px;
    box-shadow: 0 4px 14px rgba(0,0,0,0.18);
  }
  .card--front {
    top: 120px;
    background: var(--navy);
    color: var(--paper);
    display: flex;
    flex-direction: column;
    align-items: center;
    justify-content: center;
  }
  .brand {
    display: flex;
    align-items: center;
    gap: 14px;
  }
  .brand__dot {
    width: 30px;
    height: 30px;
    border-radius: 50%;
    background: var(--leaf);
  }
  .brand__name {
    font-weight: 900;
    font-size: 64px;
    letter-spacing: 4px;
    line-height: 1;
  }
  .card--front .brand__name { color: var(--paper); }
  .services {
    margin-top: 54px;
    text-align: center;
    font-weight: 700;
    font-size: 17px;
    letter-spacing: 1px;
    line-height: 1.35;
    text-transform: uppercase;
  }
  .card--back {
    top: 520px;
    background: var(--paper);
    padding: 36px 34px;
  }
  .card--back .brand__name {
    color: var(--navy-text);
    font-size: 48px;
  }
  .person {
    margin-top: 46px;
  }
  .person__name {
    color: var(--navy-text);
    font-weight: 700;
    font-size: 19px;
    letter-spacing: 0.5px;
    text-transform: uppercase;
  }
  .person__title {
    margin-top: 6px;
    color: var(--leaf);
    font-size: 16px;
    line-height: 1.5;
  }
  .contact {
    margin-top: 36px;
    list-style: none;
    font-size: 17px;
    line-height: 1.55;
    color: var(--leaf);
  }
  .contact__label {
    color: var(--navy-text);
    font-weight: 700;
    margin-right: 4px;
  }
</style>
</head>
<body>
  <section class="card card--front">
    <div class="brand">
      <span class="brand__dot"></span>
      <span class="brand__name">QTR</span>
    </div>
    <p class="services">
      Applied Behavior Analysis - Parent/Teacher Training -<br>
      Social Skills Training - Tutoring
    </p>
  </section>

  <section class="card card--back">
    <div class="brand">
      <span class="brand__name">QTR</span>
    </div>
    <div class="person">
      <h1 class="person__name">Marisol Vega, B.A.</h1>
      <p class="person__title">Board Certified Asst.<br>Behavior Analyst (BCABA)</p>
    </div>
    <ul class="contact">
      <li><span class="contact__label">T:</span>786-555-0142</li>
      <li><span class="contact__label">E:</span>vega.m.cba@mail.com</li>
    </ul>
  </section>
</body>
</html>
```